Professional Services - letterhead / business cards

The company (veltaro holdings) will provide services to Investment Funds and large investors in Spain. I have recently chosen a logo that I am attaching.

I would like a simple stationary design that i could use as letter head, business cards and "with compliments" cards.

I am not quite sure which color I will mostly use for the logo, in the email signature I will probably lean towards the white background and grey letters. I am attaching my favourite options.

Target Market(s)

Large Multinationals, Investment funds and Law firms

Industry/Entity Type

Business

Requirements
Must have
• my details are:
Luis R. Andrade
Veltaro Holdings S.L.
Casa de Valdehondo
Calle del Olmo Tardío 42
28017 Madrid
T: +34 (91) 807-3356
M: +34 (655) 718-904
e-mail: landrade@veltaroholdings.example

```html
<!DOCTYPE html>
<html lang="en">
<head>
<meta charset="utf-8">
<title>Veltaro Holdings – Business Cards</title>
<link rel="stylesheet" href="https://fonts.googleapis.com/css2?family=Didact+Gothic&display=swap">
<style>
  :root {
    --navy: #0d1270;
    --navy-ink: #1a1f6e;
    --white: #ffffff;
    --rule-grey: #c9cad3;
    --text-grey: #5a5d78;
    --backdrop: #e6e4e1;
  }
  * { box-sizing: border-box; margin: 0; padding: 0; }
  html, body {
    width: 1200px; height: 588px; overflow: hidden;
    background: var(--backdrop);
    font-family: "Didact Gothic", "Century Gothic", sans-serif;
  }
  .canvas {
    position: relative; width: 1200px; height: 588px;
  }
  .card {
    position: absolute; top: 151px;
    width: 510px; height: 286px;
    border-radius: 14px; overflow: hidden;
    box-shadow: 0 6px 18px rgba(0,0,0,0.18);
  }

  /* Back side */
  .card-back {
    left: 60px;
    background: var(--navy);
    color: var(--white);
    display: flex; flex-direction: column; align-items: center; justify-content: center;
  }
  .card-back .brand-name {
    font-size: 40px; letter-spacing: 0.5px; line-height: 1;
  }
  .card-back .website {
    margin-top: 26px; font-size: 13px; letter-spacing: 3px;
  }

  /* Front side */
  .card-front {
    left: 630px;
    background: var(--white);
    color: var(--navy-ink);
  }
  .card-front .brand-name {
    position: absolute; left: 34px; top: 30px;
    font-size: 36px; line-height: 1; color: var(--navy-ink);
  }
  .holder {
    position: absolute; left: 34px; top: 96px;
    font-size: 15px; letter-spacing: 1px;
  }
  .holder .holder-name { text-transform: uppercase; font-size: 17px; }
  .holder .holder-company { font-size: 11px; letter-spacing: 0.3px; margin-left: 6px; }
  .address {
    position: absolute; right: 258px; top: 128px;
    text-align: right; font-size: 11px; line-height: 17px; color: var(--text-grey);
  }
  .contacts {
    position: absolute; left: 268px; top: 128px;
    list-style: none; font-size: 11px; line-height: 17px; color: var(--text-grey);
  }
  .contacts li { display: flex; align-items: center; gap: 8px; }
  .contacts svg { width: 10px; height: 10px; fill: var(--navy-ink); flex: none; }
  .front-band {
    position: absolute; left: 0; right: 0; bottom: 0; height: 84px;
    background: var(--navy);
    border-top: 3px solid var(--rule-grey);
  }
</style>
</head>
<body>
<main class="canvas">
  <section class="card card-back" aria-label="Business card, back">
    <p class="brand-name">veltaro holdings</p>
    <p class="website">www.veltaroholdings.example</p>
  </section>

  <section class="card card-front" aria-label="Business card, front">
    <p class="brand-name">veltaro holdings</p>
    <p class="holder">
      <span class="holder-name">Luis R. Andrade,</span><span class="holder-company">Veltaro Holdings S.L.</span>
    </p>
    <address class="address">
      Casa de Valdehondo<br>
      Calle del Olmo Tardío 42<br>
      28017 Madrid
    </address>
    <ul class="contacts">
      <li>
        <svg viewBox="0 0 10 10" aria-hidden="true"><path d="M2 0.5 L3.6 0.5 L4.3 2.8 L3.2 3.7 Q4.2 5.8 6.3 6.8 L7.2 5.7 L9.5 6.4 L9.5 8 Q9.5 9.5 8 9.5 Q0.5 9 0.5 2 Q0.5 0.5 2 0.5 Z"/></svg>
        <span>+34 (91) 807-3356</span>
      </li>
      <li>
        <svg viewBox="0 0 10 10" aria-hidden="true"><path d="M2.5 0 H7.5 V10 H2.5 Z M3.3 1.2 V7.8 H6.7 V1.2 Z"/></svg>
        <span>+34 (655) 718-904</span>
      </li>
      <li>
        <svg viewBox="0 0 10 10" aria-hidden="true"><path d="M0 2 H10 V8 H0 Z M1 3 L5 5.8 L9 3 V2.8 H1 Z"/></svg>
        <span>landrade@veltaroholdings.example</span>
      </li>
    </ul>
    <div class="front-band"></div>
  </section>
</main>
</body>
</html>
```